Startup High Tech Software Company Needs a Web Design (4 pages)

We need a web design for a startup high tech software company based in Brazil called Vexlo. We are known to build extremely fast softwares with high qualities for web and mobile (Verdant and Aerio) applications.
We still don't have all the content to build the institutional web site, but we'd like to have the design already so we can change the content on demand later.
Basically we're requesting a home page and 3 templates of internal pages with spaces to videos and images.
Below are some examples of sites (please ignore the style, this is just to show the distribution of the main content):
Home: http://www.prondel.com.br/
Internal pages: http://www.qorvath.com/brightglobe/us/en/embedded_systems/industries/index.html
http://www-01.qorvath.com/software/lucent/solutions/automotive/
http://www.qorvath.com/brightglobe/us/en/embedded_systems/overview/index.html?lnk=ushpls1

The header and footer of Qorvath's web site's positions looks good for us (not the same style).

The first impression should be representing exactly what we are, fast and innovative company with high quality professionals.

Please consider the logos attached. We'd like to have a web site that combines with these logos. You can use either one (horizontal or vertical) depending on the place it is located.

Target Market(s)

CIO, IT managers of mid to big size companies

Industry/Entity Type

Automotive

Requirements
Must have
• HTML, CSS (responsive CSS is preferred) and images like buttons with no text inside, because the web site is going to have different languages so we can edit them easily.
Like Qorvath, some link or combobox to change the language.
Nice to have
• Timer to change the main content of the home page (not flash).
Should not have
• Flash

```html
<!DOCTYPE html>
<html lang="en">
<head>
<meta charset="utf-8">
<title>Vexlo — Mobile Applications</title>
<link href="https://fonts.googleapis.com/css2?family=Open+Sans:wght@300;400;600;700&family=Roboto+Condensed:wght@400;700&display=swap" rel="stylesheet">
<style>
:root{
  --ink:#1a1a1a;
  --blue:#1e4f8c;
  --blue-dark:#17406f;
  --text:#555;
  --muted:#777;
  --band:#ececec;
  --footer:#141414;
  --footer-deep:#0b0b0b;
  --footer-head:#3f6a9a;
  --hero-a:#f6ead2;
  --hero-b:#f0c98a;
}
*{box-sizing:border-box;margin:0;padding:0}
html,body{width:781px;height:1200px;overflow:hidden;background:#fff}
body{position:relative;font-family:"Open Sans",Arial,sans-serif;color:var(--text)}
.abs{position:absolute}

/* top bar */
.topbar{left:0;top:0;width:781px;height:31px;background:#0c0c0c}
.tb-btn{top:6px;height:21px;font:400 9px/21px "Roboto Condensed",sans-serif;color:#fff;text-align:center;text-transform:uppercase}
.tb-login{left:369px;width:46px;background:var(--blue)}
.tb-register{left:415px;width:79px;background:#2a2a2a}
.tb-search{left:498px;top:5px;width:142px;height:22px;background:#fff;border-radius:2px;font-size:7px;color:#999;padding:6px 10px}
.tb-lang{left:644px;top:5px;width:64px;height:22px;background:#fff;border-radius:2px;font-size:7px;color:#333;padding:6px 8px}

/* header */
.header{left:0;top:31px;width:781px;height:57px;background:linear-gradient(#eef3f7,#dde6ee)}
.logo{left:66px;top:45px;display:flex;align-items:center;gap:6px}
.logo-mark{width:26px;height:26px;background:var(--blue)}
.logo-name{font:700 26px/1 "Open Sans",sans-serif;color:var(--blue);letter-spacing:1px}
.nav{top:54px;font:400 10px/24px "Roboto Condensed",sans-serif;color:#222;text-transform:uppercase}
.nav-active{left:355px;width:42px;background:var(--blue);color:#fff;text-align:center}

/* hero */
.hero{left:0;top:88px;width:781px;height:361px;background:radial-gradient(ellipse at 55% 40%,#fbf3e4 0%,var(--hero-a) 40%,var(--hero-b) 100%)}
.hero-photo{left:0;top:88px;width:375px;height:361px;background:linear-gradient(100deg,#c99e7a 0%,#e8c3a0 40%,rgba(240,220,190,0) 100%)}
.hero-title{left:391px;top:130px;font:300 29px/32px "Open Sans",sans-serif;color:var(--ink)}
.hero-text{left:391px;top:200px;width:263px;font-size:8.6px;line-height:15.6px;color:#6a5a44;text-align:justify}
.hero-cta{left:390px;top:280px;width:151px;height:29px;background:#111;color:#fff;font:400 12px/29px "Roboto Condensed",sans-serif;padding-left:11px}
.hero-cta span{position:absolute;right:8px;top:8px;width:13px;height:13px;border-radius:50%;background:#555}
.store{top:346px;width:143px;height:37px;background:linear-gradient(#fff,#eee);border:1px solid #ddd;border-radius:2px}
.store-ico{position:absolute;left:0;top:0;width:40px;height:35px;border-right:1px solid #ddd}
.store-txt{position:absolute;left:49px;top:7px;font-size:8px;color:#999;line-height:10px}
.store-txt b{display:block;font-size:11px;color:#555;font-weight:600;line-height:13px}
.arrows{left:635px;top:402px}

/* services */
.svc-shade{width:60px;height:98px;background:linear-gradient(90deg,rgba(0,0,0,0),rgba(0,0,0,.06))}
.svc-title{font:400 14px/1 "Open Sans",sans-serif;color:var(--blue-dark);white-space:nowrap}
.svc-text{width:138px;font-size:8.6px;line-height:11.8px;color:#666;text-align:justify}
.svc-more{width:70px;height:20px;background:#eee;font:400 7.5px/20px "Roboto Condensed",sans-serif;color:#666;text-align:center}

/* welcome */
.welcome-title{left:0;width:781px;top:678px;text-align:center;font:400 16px/1 "Open Sans",sans-serif;color:var(--blue-dark)}
.welcome-text{left:86px;width:610px;top:708px;text-align:center;font-size:8.8px;line-height:15.6px;color:#777}

/* band */
.band{left:0;top:782px;width:781px;height:215px;background:var(--band)}
.band-col{top:782px;width:1px;height:215px;background:#d6d6d6}
.band-ico{width:29px;height:29px;border-radius:50%;background:var(--blue)}
.band-head{font:300 17px/29px "Open Sans",sans-serif;color:var(--blue-dark);text-transform:uppercase}
.video{left:68px;top:829px;width:191px;height:115px;background:#222;border:3px solid #444}
.btn-dark{height:22px;background:#111;color:#fff;font:700 9.5px/22px "Roboto Condensed",sans-serif;text-align:center}
.testi-photo{left:285px;top:837px;width:63px;height:63px;border-radius:50%;background:linear-gradient(135deg,#cfd9e0,#8aa2b4);border:3px solid #fff}
.testi-quote{left:357px;top:842px;width:135px;font-size:8.4px;line-height:15.6px;color:#444}
.testi-quote em{color:#e08a1e}
.testi-by{left:455px;top:938px;font-size:10px;color:var(--blue-dark)}
.field{left:525px;width:197px;height:24px;background:#fff;border-radius:8px;font-size:7.5px;color:#333;padding:6px 12px}

/* footer */
.footer{left:0;top:997px;width:781px;height:154px;background:var(--footer)}
.f-col{top:1012px;font-size:8.8px;color:#eee}
.f-col h4{font-weight:400;color:var(--footer-head);font-size:9px;margin-bottom:8px}
.f-col li{list-style:none;line-height:18.2px}
.f-col li::before{content:"▸";font-size:7px;margin-right:6px}
.bottom{left:0;top:1151px;width:781px;height:49px;background:var(--footer-deep)}
.copy{left:73px;top:1166px;font-size:9px;color:#ccc}
.soc{top:1165px;width:16px;height:16px;background:#3b6aa0}
</style>
</head>
<body>

<div class="abs topbar"></div>
<div class="abs tb-btn tb-login">Login</div>
<div class="abs tb-btn tb-register">Register</div>
<div class="abs tb-search">Search</div>
<div class="abs tb-lang">Eng ▾</div>

<div class="abs header"></div>
<div class="abs logo"><span class="logo-mark"></span><span class="logo-name">VEXLO</span></div>
<div class="abs nav nav-active">Home</div>
<div class="abs nav" style="left:410px">About Us</div>
<div class="abs nav" style="left:473px">Services</div>
<div class="abs nav" style="left:533px">Applications</div>
<div class="abs nav" style="left:613px">Contact Us</div>

<div class="abs hero"></div>
<div class="abs hero-photo" role="img" aria-label="Hand holding a smartphone showing a friends map app"></div>
<h1 class="abs hero-title">We make Aerio and<br>Verdant Applications</h1>
<p class="abs hero-text">Curabitur luctus, sem a rhoncus laoreet, turpis mauris imperdiet odio, nec pellentesque dolor lorem vitae lorem. Nulla sit amet consequat tellus. Donec pharetra iaculis sapien, et fringilla libero mattis in. Nullam accumsan hendrerit tempus.</p>
<div class="abs hero-cta">VIEW APPLICATIONS<span></span></div>
<div class="abs store" style="left:384px">
  <div class="store-ico"><svg width="40" height="35"><rect x="15" y="8" width="11" height="19" rx="2" fill="none" stroke="#888" stroke-width="1.5"/></svg></div>
  <div class="store-txt">Available on the<b>Apps Depot</b></div>
</div>
<div class="abs store" style="left:534px">
  <div class="store-ico"><svg width="40" height="35"><rect x="12" y="12" width="16" height="14" rx="1" fill="#888"/><path d="M16 12v-2a4 4 0 0 1 8 0v2" fill="none" stroke="#888" stroke-width="1.5"/></svg></div>
  <div class="store-txt">Available in<b>Gadget Bazaar</b></div>
</div>
<svg class="abs arrows" width="40" height="30"><path d="M14 4 4 14l10 10M26 4l10 10-10 10" fill="none" stroke="#fff" stroke-width="3"/></svg>

<!-- services -->
<div class="abs svc-shade" style="left:227px;top:467px"></div>
<div class="abs svc-shade" style="left:444px;top:467px"></div>
<div class="abs svc-shade" style="left:227px;top:570px"></div>
<div class="abs svc-shade" style="left:444px;top:570px"></div>

<svg class="abs" style="left:90px;top:482px" width="24" height="44"><rect x="2" y="2" width="20" height="40" rx="4" fill="none" stroke="#333" stroke-width="3"/><circle cx="12" cy="36" r="2" fill="#333"/></svg>
<div class="abs svc-title" style="left:127px;top:478px">Phone Applications</div>
<p class="abs svc-text" style="left:128px;top:497px">Pellentesque id urna pulvinar nulla bibendum vulputate augue vitae hendrerit volutpat.</p>
<div class="abs svc-more" style="left:86px;top:540px">VIEW MORE »</div>

<svg class="abs" style="left:300px;top:484px" width="36" height="40"><rect x="2" y="2" width="32" height="36" rx="4" fill="none" stroke="#333" stroke-width="3"/><rect x="8" y="9" width="20" height="22" fill="#333"/></svg>
<div class="abs svc-title" style="left:346px;top:478px">Verdant Applications</div>
<p class="abs svc-text" style="left:347px;top:497px">Pellentesque id urna pulvinar nulla bibendum vulputate augue vitae hendrerit volutpat.</p>
<div class="abs svc-more" style="left:300px;top:540px">VIEW MORE »</div>

<svg class="abs" style="left:514px;top:486px" width="40" height="36"><rect x="2" y="2" width="36" height="24" rx="2" fill="none" stroke="#333" stroke-width="3"/><rect x="14" y="26" width="12" height="5" fill="#333"/><rect x="8" y="31" width="24" height="3" fill="#333"/></svg>
<div class="abs svc-title" style="left:564px;top:478px">Aerio Applications</div>
<p class="abs svc-text" style="left:565px;top:497px">Pellentesque id urna pulvinar nulla bibendum vulputate augue vitae hendrerit volutpat.</p>
<div class="abs svc-more" style="left:514px;top:540px">VIEW MORE »</div>

<svg class="abs" style="left:89px;top:583px" width="28" height="42"><rect x="2" y="2" width="24" height="38" rx="4" fill="none" stroke="#333" stroke-width="3"/><rect x="8" y="17" width="12" height="10" fill="#333"/><path d="M10 17v-3a4 4 0 0 1 8 0v3" fill="none" stroke="#333" stroke-width="2"/></svg>
<div class="abs svc-title" style="left:127px;top:579px">MobileSecurity Apps</div>
<p class="abs svc-text" style="left:128px;top:598px">Pellentesque id urna pulvinar nulla bibendum vulputate augue vitae hendrerit volutpat.</p>
<div class="abs svc-more" style="left:86px;top:642px">VIEW MORE »</div>

<svg class="abs" style="left:300px;top:585px" width="38" height="38"><rect x="2" y="22" width="8" height="16" fill="#333"/><rect x="14" y="14" width="8" height="24" fill="#333"/><rect x="26" y="6" width="10" height="32" fill="#333"/><path d="M2 12 12 2M6 2h6v6" fill="none" stroke="#333" stroke-width="2"/></svg>
<div class="abs svc-title" style="left:346px;top:579px">Business Type Apps</div>
<p class="abs svc-text" style="left:347px;top:598px">Pellentesque id urna pulvinar nulla bibendum vulputate augue vitae hendrerit volutpat.</p>
<div class="abs svc-more" style="left:300px;top:642px">VIEW MORE »</div>

<svg class="abs" style="left:513px;top:588px" width="44" height="36"><circle cx="13" cy="10" r="6" fill="#333"/><circle cx="30" cy="8" r="7" fill="#333"/><path d="M1 34a12 12 0 0 1 24 0zM16 34a14 14 0 0 1 28 0z" fill="#333"/></svg>
<div class="abs svc-title" style="left:565px;top:579px">Lifestyle Apps</div>
<p class="abs svc-text" style="left:565px;top:598px">Pellentesque id urna pulvinar nulla bibendum vulputate augue vitae hendrerit volutpat.</p>
<div class="abs svc-more" style="left:514px;top:642px">VIEW MORE »</div>

<h2 class="abs welcome-title">Welcome to Vexlo</h2>
<p class="abs welcome-text">Sed ut perspiciatis unde omnis iste natus error sit voluptatem accusantium doloremque laudantium, totam rem aperiam, eaque ipsa quae ab illo inventore veritatis et quasi architecto beatae vitae dicta sunt explicabo. Nemo enim ipsam voluptatem quia voluptas sit aspernatur aut odit aut fugit, sed quia consequuntur magni dolores eos qui ratione voluptatem sequi nesciunt. Neque porro quisquam est, qui dolorem ipsum quia dolor sit amet, consectetur, adipisci velit, sed quia non numquam eius modi tempora incidunt ut labore et dolore magnam aliquam quaerat voluptatem.</p>

<!-- band -->
<div class="abs band"></div>
<div class="abs band-col" style="left:275px"></div>
<div class="abs band-col" style="left:510px"></div>

<svg class="abs band-ico" style="left:60px;top:795px" viewBox="0 0 29 29"><circle cx="14.5" cy="14.5" r="14.5" fill="#1e4f8c"/><path d="M9 13v-3h9l-2-2M20 16v3h-9l2 2" fill="none" stroke="#fff" stroke-width="2"/></svg>
<div class="abs band-head" style="left:98px;top:795px">How it works</div>
<div class="abs video" role="img" aria-label="Video player showing the Vexlo intro"></div>
<svg class="abs" style="left:153px;top:869px" width="22" height="24"><path d="M2 2 20 12 2 22z" fill="#fff"/></svg>
<div class="abs btn-dark" style="left:71px;top:960px;width:72px">Read more</div>

<svg class="abs band-ico" style="left:294px;top:795px" viewBox="0 0 29 29"><circle cx="14.5" cy="14.5" r="14.5" fill="#1e4f8c"/><circle cx="14.5" cy="11" r="4" fill="#fff"/><path d="M7 22a7.5 6 0 0 1 15 0z" fill="#fff"/></svg>
<div class="abs band-head" style="left:332px;top:795px">Testimonials</div>
<div class="abs testi-photo" role="img" aria-label="Portrait photo of a customer"></div>
<p class="abs testi-quote"><em>Sed ut perspiciatis unde omnis iste natus error sit voluptatem</em> accusantium doloremque laudantium, totam rem aperiam, eaque ipsa quae ab illo inventore veritatis et quasi architecto</p>
<div class="abs testi-by">- Anika</div>
<div class="abs btn-dark" style="left:298px;top:960px;width:72px">Read more</div>

<svg class="abs band-ico" style="left:535px;top:795px" viewBox="0 0 29 29"><circle cx="14.5" cy="14.5" r="14.5" fill="#1e4f8c"/><path d="M9 20c2-7 6-10 12-12-2 6-5 10-12 12z" fill="#fff"/></svg>
<div class="abs band-head" style="left:575px;top:795px">Request a quote</div>
<div class="abs field" style="top:835px">Name</div>
<div class="abs field" style="top:868px">Email</div>
<div class="abs field" style="top:901px;height:38px">Message</div>
<div class="abs btn-dark" style="left:594px;top:952px;width:72px">Submit</div>

<!-- footer -->
<div class="abs footer"></div>
<div class="abs f-col" style="left:73px"><h4>Footer Links Header</h4><ul><li>Aliquam nec</li><li>Duis ultriciessem</li><li>Aliquam vehi</li><li>Etiam euismod</li><li>Nulla lobortis dolo</li><li>Nunc a scelerisque</li></ul></div>
<div class="abs f-col" style="left:211px"><h4>Footer Links Header</h4><ul><li>Aliquam nec</li><li>Duis ultriciessem</li><li>Aliquam vehi</li><li>Etiam euismod</li><li>Nulla lobortis dolo</li><li>Nunc a scelerisque</li></ul></div>
<div class="abs f-col" style="left:349px"><h4>Footer Links Header</h4><ul><li>Aliquam nec</li><li>Duis ultriciessem</li><li>Aliquam vehi</li><li>Etiam euismod</li><li>Nulla lobortis dolo</li><li>Nunc a scelerisque</li></ul></div>
<div class="abs f-col" style="left:486px"><h4>Footer Links Header</h4><ul><li>Aliquam nec</li><li>Duis ultriciessem</li><li>Aliquam vehi</li><li>Etiam euismod</li><li>Nulla lobortis dolo</li><li>Nunc a scelerisque</li></ul></div>
<div class="abs f-col" style="left:624px"><h4>Footer Links Header</h4><ul><li>Aliquam nec</li><li>Duis ultriciessem</li><li>Aliquam vehi</li><li>Etiam euismod</li><li>Nulla lobortis dolo</li><li>Nunc a scelerisque</li></ul></div>

<div class="abs bottom"></div>
<div class="abs copy">Copyright © 2013 &nbsp;www.vexlo.com &nbsp; All rights reserved.</div>
<div class="abs soc" style="left:626px"></div>
<div class="abs soc" style="left:648px"></div>
<div class="abs soc" style="left:670px"></div>
<div class="abs soc" style="left:692px"></div>

</body>
</html>
```